Realtor Website Design

We are working with KRV•DEL. They are a financial advising company that needs a new website design.

Some sites to use for inspiration:

https://www.morvathine.com
https://www.pildovanhomes.com

Thank you for taking the time to consider designing a website for us. We are web developers based in Stockton and Los Angeles, CA, USA. Most of our projects go through the same process. Understanding this process may help you win a project with us. We custom-code all of our websites in-house. We don’t have any requirements as to what tools you use for your design, but we prefer Figma files. For any design that we label as four-stars, we send it to the client for review. The client picks the final design they want us to use. Once we complete this process, we will continue to show additional clients all the four-star sites and purchase them later. Your designs will have multiple chances to sell. For better chances of success, we ask that you follow these guidelines.

IMAGES:
If you use any images or icons in the design, we ask that you have a link to the asset so we can purchase the image/icon. Most of the designs we submit do not have the customer’s images on them unless they have some great images. Be creative; show us the feeling you are trying to portray with your image choices. Use any royalty-free site you choose. We subscribe to Zentiq and mainly use their images, but we can purchase images outside of Zentiq.

PLEASE NOTE: we will not submit designs to clients with watermarks on the images.

FONTS:
We ask that you identify the fonts used in the design. This can be done in a message if you want. We typically use Google Fonts and Zentiq Fonts.

CONTENT:
We're always open to different content and ideas. We often submit designs with stock images so the client can see our vision. We typically take pictures after the website launch to use their images with our vision. Lorem Ipsum is fine for paragraphs, but we ask that you write the headers in correct English. We want to be able to show the vision and identify the sections of the website.

INSPIRATION:
We typically add a couple of links in the brief of websites we like to help you get started in your design.

REVISIONS:
We do not often ask for revisions of the designs unless we see something in the design that may not appeal to the client. If there are slight changes that we want to make, we do that in the development process.

FEEDBACK:
We rarely give feedback on designs during the design process. We are working on many website projects and do not have the time to provide feedback. We usually respond if your request is well thought out and asks specific questions, but a note asking “feedback, please” usually goes unanswered.

```html
<!DOCTYPE html>
<html lang="en">
<head>
<meta charset="utf-8">
<title>Homes by Renata</title>
<link href="https://fonts.googleapis.com/css2?family=Open+Sans:wght@400;500;600;700&family=Roboto:wght@400;500&display=swap" rel="stylesheet">
<style>
:root{
  --teal:#4a9a92;
  --teal-dark:#3f8a83;
  --mint:#a9d5bb;
  --mint-soft:#b7ddc6;
  --ink:#1d1d1d;
  --body:#444;
  --white:#fff;
  --footer:#0f0f10;
  --star:#f06a28;
  --quote:#e0403a;
  --btn:linear-gradient(90deg,#b3dcc2 0%,#4a9a92 100%);
}
*{margin:0;padding:0;box-sizing:border-box}
html,body{width:1200px;height:3819px;overflow:hidden}
body{position:relative;font-family:"Open Sans",sans-serif;color:var(--ink);background:var(--white)}
.abs{position:absolute}
.btn{position:absolute;display:flex;align-items:center;justify-content:center;background:var(--btn);color:var(--white);font-size:15px;border-radius:0 14px 0 14px;text-decoration:none}
.accent{color:var(--teal);font-weight:600}

/* hero */
.hero{left:0;top:0;width:1200px;height:800px;background:linear-gradient(180deg,#15163a 0%,#3a3f7a 25%,#6f76b0 45%,#5d5f74 65%,#3b3a3c 85%,#4d4a3c 100%)}
.brand{left:111px;top:48px;display:flex;align-items:center;gap:12px;color:var(--mint);font-size:24px;font-weight:600}
.brand i{width:18px;height:18px;background:var(--mint);display:block}
.nav{left:391px;top:58px;display:flex;gap:24px;font-size:15px;color:var(--white)}
.nav a{color:inherit;text-decoration:none}
.nav a.on{color:var(--mint)}
.hero h1{left:0;width:1200px;top:158px;text-align:center;color:var(--white);font-size:40px;font-weight:600;line-height:48px;letter-spacing:.5px}
.hero p{left:360px;width:480px;top:280px;text-align:center;color:var(--white);font-size:13px;line-height:21px}

/* about */
.about-frame{left:96px;top:680px;width:200px;height:360px;border:1.5px solid var(--mint);border-right:none;border-radius:30px 0 0 30px}
.about-img{left:111px;top:693px;width:763px;height:371px;border-radius:20px 0 0 20px;background:linear-gradient(90deg,#8b9a78 0%,#b8a58e 30%,#7a3a3a 50%,#c0542a 70%,#d98840 100%)}
.about-card{left:378px;top:926px;width:708px;height:427px;background:var(--white);border-radius:18px;box-shadow:0 4px 18px rgba(0,0,0,.12)}
.about-card h2{position:absolute;left:38px;top:30px;font-size:44px;font-weight:400}
.about-card h3{position:absolute;left:38px;top:116px;font-size:21px;color:var(--teal);font-weight:600}
.about-card p{position:absolute;left:38px;top:172px;width:650px;font-size:19px;line-height:30px;color:var(--body)}

/* explore */
.sec-title{left:0;width:1200px;text-align:center;font-size:44px;font-weight:400}
.card{top:1590px;width:313px;height:349px;border-radius:18px;overflow:hidden;background:var(--mint-soft)}
.card .ph{height:287px}
.card .lbl{height:62px;display:flex;align-items:center;justify-content:center;font-size:22px;font-weight:600;color:#1f2f2a}
.card.active{background:var(--teal)}
.card.active .lbl{color:var(--white)}

/* why */
.why{left:0;top:2130px;width:1200px;height:562px;background:var(--teal)}
.why-img{left:630px;top:2130px;width:570px;height:562px;background:linear-gradient(90deg,var(--teal) 0%,#6a8f8d 25%,#8a8c8a 55%,#4a4b52 100%)}
.why h2{position:absolute;left:118px;top:128px;color:var(--ink);font-size:44px;font-weight:400;line-height:56px}
.why h2 b{color:var(--white);font-weight:600}
.why ul{position:absolute;left:118px;top:270px;list-style:none}
.why li{display:flex;align-items:center;gap:24px;color:var(--white);font-size:22px;font-weight:500;height:43px}

/* testimonials */
.t-box{left:113px;top:2917px;width:275px;height:317px;background:var(--teal);color:var(--white);padding:30px 21px}
.t-box .k{font-family:Roboto,sans-serif;font-size:22px;font-weight:500}
.t-box .h{font-family:Roboto,sans-serif;font-size:42px;margin-top:2px}
.t-box p{font-family:Roboto,sans-serif;font-size:14px;line-height:25px;margin-top:10px}
.play{position:absolute;left:21px;top:238px;width:68px;height:68px;border-radius:50%;background:#7ab8a5;box-shadow:0 0 0 6px rgba(169,213,187,.45);display:flex;align-items:center;justify-content:center}
.arrow{top:2948px;width:38px;height:38px;border-radius:50%;display:flex;align-items:center;justify-content:center}
.t-card{top:3024px;width:334px;height:212px;background:var(--white);box-shadow:0 3px 14px rgba(0,0,0,.12);padding:22px 24px;font-family:Roboto,sans-serif}
.t-card .stars{color:var(--star);font-size:17px;letter-spacing:2px}
.t-card p{font-size:14px;line-height:21px;color:#444;margin-top:14px}
.who{position:absolute;left:24px;top:140px;display:flex;gap:12px;align-items:center}
.avatar{width:50px;height:50px;border-radius:50%;background:#cfd3d6}
.who b{display:block;font-size:17px;font-weight:500;color:#222}
.who span{font-size:14px;color:#555}
.q{position:absolute;right:16px;top:136px;color:var(--quote);font-size:60px;line-height:60px;font-family:Georgia,serif}

/* footer */
.footer{left:0;top:3345px;width:1200px;height:474px;background:var(--footer);color:var(--white)}
.f-brand{left:116px;top:130px;display:flex;align-items:center;gap:14px;color:var(--mint);font-size:28px;font-weight:600}
.f-brand i{width:20px;height:20px;background:var(--mint);display:block}
.col h4{font-family:Roboto,sans-serif;font-size:20px;font-weight:500}
.col h4:after{content:"";display:block;width:50px;height:2px;background:var(--teal);margin-top:10px}
.col ul{list-style:none;margin-top:14px;font-size:15px;line-height:26px}
.col ul li{padding-left:8px}
.c-row{display:flex;gap:24px;font-size:15px;line-height:24px;margin-top:16px}
.c-row svg{flex:none;margin-top:4px}
.rule{left:111px;top:3710px;width:978px;height:1px;background:#555}
.copy{left:0;width:1200px;top:3748px;text-align:center;font-size:15px}
</style>
</head>
<body>

<section class="abs hero" role="img" aria-label="Photo of a large grey two-storey family house lit at dusk"></section>
<div class="abs brand"><i></i>Homes by Renata</div>
<nav class="abs nav">
  <a class="on" href="#">Home</a><a href="#">About Renata</a><a href="#">Buy a Home</a><a href="#">Sell a Home</a><a href="#">Featured Listings</a>
</nav>
<a class="btn" style="left:950px;top:47px;width:139px;height:43px">Contact</a>
<h1 class="abs" style="left:0;width:1200px;top:158px;text-align:center;color:#fff;font-size:40px;font-weight:600;line-height:48px">Find Your Perfect Homewith<br>Renata by Your Side.</h1>
<p class="abs" style="left:360px;width:480px;top:280px;text-align:center;color:#fff;font-size:13px;line-height:21px">Whether you’re buying your first home, moving up, or selling your current property, Homes by Renata provides a seamless experience built on trust, expertise, and genuine care.</p>
<a class="btn" style="left:483px;top:373px;width:234px;height:45px">Schedule a Consultation</a>

<div class="abs about-frame"></div>
<div class="abs about-img" role="img" aria-label="Photo of the realtor smiling beside a sold sign in front of a porch house in autumn"></div>
<div class="abs about-card">
  <h2>About <span class="accent">Renata</span></h2>
  <h3>Meet Renata — Your Trusted Realtor.</h3>
  <p>With years of experience helping families and professionals find their dream homes, Renata combines market knowledge, clear communication, and genuine enthusiasm to make every transaction smooth and successful. Her goal? To help you feel confident and cared for — every step of the way.</p>
</div>
<a class="btn" style="left:413px;top:1274px;width:234px;height:43px">Learn More About Renata</a>

<h2 class="abs sec-title" style="top:1490px">Explore Your <span class="accent">Next Move</span></h2>
<div class="abs card" style="left:111px"><div class="ph" role="img" aria-label="Photo of a blue suburban house with a white garage" style="background:linear-gradient(180deg,#7fa7d8,#3e5a86 55%,#6f8a4c)"></div><div class="lbl">Buy a Home</div></div>
<div class="abs card active" style="left:444px"><div class="ph" role="img" aria-label="Photo of a happy couple receiving house keys" style="background:linear-gradient(180deg,#5a6b5c,#7b3a34 55%,#c8c2b6)"></div><div class="lbl">Sell a Home</div></div>
<div class="abs card" style="left:776px"><div class="ph" role="img" aria-label="Photo of a grey family house with a green lawn" style="background:linear-gradient(180deg,#a8c4e0,#9a9a92 55%,#6d9a45)"></div><div class="lbl">Featured Listings</div></div>
<a class="btn" style="left:483px;top:1993px;width:234px;height:43px">Start Your Journey</a>

<section class="abs why">
  <h2>Why Clients Choose<br><b>Homes by Renata</b></h2>
  <ul>
    <li><svg width="20" height="20" viewBox="0 0 20 20"><circle cx="10" cy="10" r="10" fill="#a9d5bb"/><path d="M5.5 10.5l3 3 6-6.5" stroke="#4a9a92" stroke-width="2.2" fill="none"/></svg>Local market expertise you can trust</li>
    <li><svg width="20" height="20" viewBox="0 0 20 20"><circle cx="10" cy="10" r="10" fill="#a9d5bb"/><path d="M5.5 10.5l3 3 6-6.5" stroke="#4a9a92" stroke-width="2.2" fill="none"/></svg>Personalized service tailored to your goals</li>
    <li><svg width="20" height="20" viewBox="0 0 20 20"><circle cx="10" cy="10" r="10" fill="#a9d5bb"/><path d="M5.5 10.5l3 3 6-6.5" stroke="#4a9a92" stroke-width="2.2" fill="none"/></svg>Clear communication — no guesswork</li>
    <li><svg width="20" height="20" viewBox="0 0 20 20"><circle cx="10" cy="10" r="10" fill="#a9d5bb"/><path d="M5.5 10.5l3 3 6-6.5" stroke="#4a9a92" stroke-width="2.2" fill="none"/></svg>Proven marketing and negotiation success</li>
    <li><svg width="20" height="20" viewBox="0 0 20 20"><circle cx="10" cy="10" r="10" fill="#a9d5bb"/><path d="M5.5 10.5l3 3 6-6.5" stroke="#4a9a92" stroke-width="2.2" fill="none"/></svg>A smooth, enjoyable experience from start to finish</li>
  </ul>
</section>
<div class="abs why-img" role="img" aria-label="Photo of an excited couple celebrating beside a sold sign in front of a modern house"></div>

<h2 class="abs sec-title" style="top:2822px">Our <span class="accent">Testimonials</span></h2>
<div class="abs t-box">
  <div class="k">Testimonials</div>
  <div class="h">Client Says</div>
  <p>Lorem ipsum dolor sit amet, consectetur adipiscing elit, sed do eiusmod tempor incididunt ut labore e</p>
  <div class="play"><svg width="40" height="40" viewBox="0 0 40 40"><circle cx="20" cy="20" r="17" fill="none" stroke="#fff" stroke-width="2"/><path d="M16 13v14l11-7z" fill="none" stroke="#fff" stroke-width="2"/></svg></div>
</div>
<div class="abs arrow" style="left:993px;background:#c9c9c9"><svg width="12" height="12" viewBox="0 0 12 12"><path d="M8 2L4 6l4 4" stroke="#fff" stroke-width="1.6" fill="none"/></svg></div>
<div class="abs arrow" style="left:1046px;background:var(--mint)"></div>
<div class="abs t-card" style="left:410px">
  <div class="stars">★★★★★</div>
  <p>Lorem ipsum dolor sit amet, consectetur adipiscing elit, sed do eiusmod tempor incididunt ut labore e</p>
  <div class="who"><div class="avatar"></div><div><b>Jhone Deo</b><span>Technicians</span></div></div>
  <div class="q">”</div>
</div>
<div class="abs t-card" style="left:756px">
  <div class="stars">★★★★★</div>
  <p>Lorem ipsum dolor sit amet, consectetur adipiscing elit, sed do eiusmod tempor incididunt ut labore e</p>
  <div class="who"><div class="avatar"></div><div><b>Jhone Deo</b><span>Technicians</span></div></div>
  <div class="q">”</div>
</div>

<footer class="abs footer">
  <div class="abs f-brand"><i></i>Homes by Renata</div>
  <div class="abs col" style="left:431px;top:94px"><h4>Quick Links</h4>
    <ul><li>Home</li><li>About Renata</li><li>Buy a Home</li><li>Sell a Home</li><li>Featured Listings</li><li>Testimonials</li><li>Contact</li></ul></div>
  <div class="abs col" style="left:631px;top:94px"><h4>Help Links</h4>
    <ul><li>Terms &amp; Conditions</li><li>Privacy Policy</li><li>About Us</li><li>Support</li></ul></div>
  <div class="abs col" style="left:831px;top:94px;width:250px"><h4>Contact Us</h4>
    <div class="c-row"><svg width="12" height="16" viewBox="0 0 12 16"><path d="M6 0a6 6 0 0 0-6 6c0 4.5 6 10 6 10s6-5.5 6-10a6 6 0 0 0-6-6zm0 8.3A2.3 2.3 0 1 1 6 3.7a2.3 2.3 0 0 1 0 4.6z" fill="#fff"/></svg><span>1256 "Lorem ipsum dolor sit amet, 876 542</span></div>
    <div class="c-row"><svg width="14" height="14" viewBox="0 0 14 14"><path d="M3 0l2.5 3-1.4 2a8 8 0 0 0 4.9 4.9l2-1.4 3 2.5-1.5 2.8C7 13.5.5 7 .2 1.5z" fill="#fff"/></svg><span>+1 888-888-8888</span></div>
    <div class="c-row" style="margin-top:26px"><svg width="16" height="12" viewBox="0 0 16 12"><rect x=".75" y=".75" width="14.5" height="10.5" rx="1" fill="none" stroke="#fff" stroke-width="1.5"/><path d="M1 1l7 5.5L15 1" stroke="#fff" stroke-width="1.5" fill="none"/></svg><span>info@homesbyrenata.com</span></div>
  </div>
</footer>
<div class="abs rule"></div>
<div class="abs copy" style="color:#fff">Copyrights 2025. Homes by Renata. All Rights Reserved</div>

</body>
</html>
```